Stationery International Trade Company
Coral Vantage Ltd
Stationery International Trade Company - Trade
Creative Brief
Simple
Milo Harrigan
Sales Director
Latchford St, Ashcombe
Milo.harrigan@coralvantage.com
www.coralvantage.com
We want the tagline on all stationery "Worldwide Supply Partners"

```html
<!DOCTYPE html>
<html lang="en">
<head>
<meta charset="utf-8">
<title>Coral Vantage Ltd – Business Card</title>
<link rel="stylesheet" href="https://fonts.googleapis.com/css2?family=Cinzel:wght@400;600&display=swap">
<style>
  :root {
    --page-bg: #e9e9e7;
    --card-bg: #ffffff;
    --band-dark: #3b3b3d;
    --accent-orange: #ee6a2c;
    --accent-red: #d8402a;
    --text-grey: #5f5f62;
    --text-light: #ffffff;
  }
  * { margin: 0; padding: 0; box-sizing: border-box; }
  html, body {
    width: 1200px;
    height: 914px;
    overflow: hidden;
    background: var(--page-bg);
    font-family: "Cinzel", serif;
  }
  .business-card {
    position: absolute;
    left: 100px;
    top: 172px;
    width: 1000px;
    height: 570px;
    background: var(--card-bg);
    box-shadow: 0 6px 24px rgba(0,0,0,0.12);
  }
  .brand {
    position: absolute;
    left: 250px;
    top: 110px;
    display: flex;
    align-items: center;
    gap: 26px;
  }
  .brand-mark {
    width: 92px;
    height: 92px;
    border-radius: 50%;
    background: var(--accent-orange);
    flex: none;
  }
  .brand-text { display: flex; flex-direction: column; }
  .brand-name {
    font-size: 50px;
    font-weight: 400;
    color: var(--text-grey);
    letter-spacing: 1px;
    line-height: 1;
    white-space: nowrap;
  }
  .brand-tagline {
    margin-top: 10px;
    font-size: 22px;
    color: var(--text-grey);
    letter-spacing: 2.5px;
    line-height: 1;
    white-space: nowrap;
  }
  .accent-line {
    position: absolute;
    left: 0;
    width: 100%;
    height: 3px;
    background: var(--accent-red);
  }
  .accent-line.top { top: 262px; }
  .accent-line.bottom { top: 346px; }
  .name-band {
    position: absolute;
    left: 0;
    top: 272px;
    width: 100%;
    height: 66px;
    background: var(--band-dark);
    display: flex;
    align-items: center;
    justify-content: flex-end;
    padding-right: 200px;
  }
  .person {
    color: var(--text-light);
    font-size: 24px;
    letter-spacing: 1px;
    white-space: nowrap;
  }
  .contacts {
    position: absolute;
    left: 230px;
    top: 382px;
    display: grid;
    grid-template-columns: 260px 380px;
    row-gap: 12px;
    column-gap: 10px;
  }
  .contact-item {
    display: flex;
    align-items: center;
    gap: 10px;
    min-height: 22px;
    font-size: 16px;
    color: var(--text-grey);
    letter-spacing: 0.5px;
    white-space: nowrap;
  }
  .contact-icon { width: 22px; height: 22px; flex: none; }
</style>
</head>
<body>
  <div class="business-card">
    <div class="brand">
      <div class="brand-mark"></div>
      <div class="brand-text">
        <span class="brand-name">Coral Vantage Ltd</span>
        <span class="brand-tagline">Worldwide Supply Partners</span>
      </div>
    </div>

    <div class="accent-line top"></div>
    <div class="name-band">
      <span class="person">Milo Harrigan | Sales Director</span>
    </div>
    <div class="accent-line bottom"></div>

    <div class="contacts">
      <div class="contact-item">
        <svg class="contact-icon" viewBox="0 0 22 22" aria-hidden="true">
          <circle cx="11" cy="11" r="11" fill="var(--accent-orange)"/>
          <path d="M11 4.5a4 4 0 0 0-4 4c0 3 4 8 4 8s4-5 4-8a4 4 0 0 0-4-4z" fill="#fff"/>
          <circle cx="11" cy="8.5" r="1.5" fill="var(--accent-orange)"/>
        </svg>
        <span>Latchford St, Ashcombe</span>
      </div>
      <div class="contact-item">
        <svg class="contact-icon" viewBox="0 0 22 22" aria-hidden="true">
          <circle cx="11" cy="11" r="11" fill="var(--accent-orange)"/>
          <rect x="5" y="7" width="12" height="8" fill="#fff"/>
          <path d="M5 7l6 5 6-5" fill="none" stroke="var(--accent-orange)" stroke-width="1.2"/>
        </svg>
        <span>Milo.harrigan@coralvantage.com</span>
      </div>
      <div class="contact-item">
        <svg class="contact-icon" viewBox="0 0 22 22" aria-hidden="true">
          <circle cx="11" cy="11" r="11" fill="var(--accent-orange)"/>
          <path d="M7.5 5.5l2 0 1 3-1.5 1a7 7 0 0 0 3.5 3.5l1-1.5 3 1v2a1.5 1.5 0 0 1-1.5 1.5A9 9 0 0 1 6 7a1.5 1.5 0 0 1 1.5-1.5z" fill="#fff"/>
        </svg>
        <span>0208-555-0142</span>
      </div>
      <div class="contact-item">
        <svg class="contact-icon" viewBox="0 0 22 22" aria-hidden="true">
          <circle cx="11" cy="11" r="11" fill="var(--accent-orange)"/>
          <rect x="7.5" y="4.5" width="7" height="13" rx="1.2" fill="#fff"/>
          <rect x="8.7" y="6" width="4.6" height="8.5" fill="var(--accent-orange)"/>
        </svg>
        <span>079 555 014 27</span>
      </div>
      <div class="contact-item"></div>
      <div class="contact-item">
        <svg class="contact-icon" viewBox="0 0 22 22" aria-hidden="true">
          <circle cx="11" cy="11" r="11" fill="var(--accent-orange)"/>
          <circle cx="11" cy="11" r="6" fill="none" stroke="#fff" stroke-width="1.4"/>
          <ellipse cx="11" cy="11" rx="2.6" ry="6" fill="none" stroke="#fff" stroke-width="1.2"/>
          <line x1="5" y1="11" x2="17" y2="11" stroke="#fff" stroke-width="1.2"/>
        </svg>
        <span>www.coralvantage.com</span>
      </div>
    </div>
  </div>
</body>
</html>
```